Web site for Physical Therapy Clinic

Looking for a web designer who has experience in planning & designing graphic user interfaces for web site.
You will be delivered a sitemap/flow diagram and a general visual concept and expected to deliver finished web GUI design in PSD (or any suitable) format.
RESPONSIBILITIES:
-Interpreting the sitemap/flow diagram into an user interface
-Developing a visual concept which aligns with the brands and project goals
-Building wireframes
-Design usable, technically feasible, great looking user interfaces in Photoshop(or Illustrator)
-Present your design in jpg format
-Delivering pixel perfect design ready to be converted to html/css
EXPECTATIONS:
-Adobe Creative Suite
-Deliver quality design by applying sound design practices with solid methodology, workflow & discipline.
-Manage the design process from start to finish, including gathering requirements and delivering final assets
-Strong sense of design and knowledge of typography, grid systems, color theory, usability, interactivity and information architecture principles
-Familiar with HTML, CSS, and JavaScript knowledge for optimizing design concepts around these technologies
-Familiar with standards-based, cross-browser, multi-device design
-Familiar with responsive web design/development
-Participate in estimating project efforts and delivery timelines
-Identify technical, schedule, and other project risks and provide relevant feedback
-Proactively collaborate and communicate
-Ability to multitask and prioritize multiple concurrent assignments
-High attention to detail
Corvela Physical Therapy provides personalized and high-quality therapy services. Patients are treated in two different settings; at our outpatient clinic or through home health visits. The services we provide are: Physical Therapy, Occupational Therapy, Speech Therapy and Massage Therapy.
We are looking for a designer/developer to build a fully-functional website for our business. The website needs to be:
• Fast-loading
• Mobile-compatible
• User-friendly
The following web address has been secured through namebarrow.example:
www.corvelapt.example
Tabs for the website will include...
Home
About
• History
• Team
Patients
• Services
• Insurances & payments accepted
• Coverage areas
Agencies
• Inquiries
• Forms & credentials
• Coverage areas
Therapists
• Reasons to work with us
• Career opportunities
• Application
FAQ
Contact
• Inquiries
• Locations
Breakdown of content needed on each page:
HOME
• Tagline
ABOUT
• History
• Team
PATIENTS
• Pain Management
- Neck & back pain
- Radiculopathy
- Sacroiliac Joint Syndrome
- Status Post Laminectomy
- Status Post Spinal Fusion
- Patellafemoral pain
- Arthritis: Osteoarthritis & Rheumatoid Arthritis
- Temporomandibular Joint
- Post-amputation
• Neurological Disorders
- Cerebral Vascular Accidents
- Parkinson's disease
- Multiple Sclerosis
- Traumatic & non-traumatic Brain Injury
- Spinal cord injury
- Guillain Barre
- Intracranial hemorrhage
- Diabetic neuropathy
- Post Polio Syndrome
• Work/Sport Injuries
- Carpal Tunnel Syndrome
- Disc Hernia
- Plantar Fasciitis
- Sciatica
- Frozen Shoulder
- Rotator Cuff injury/surgery
- Hip surgery
- Knee surgery: Anterior/Posterior Cruciate Ligament & Meniscal Tear
- Ankle sprain
- Tennis Elbow
- Golfer's Elbow
• Services
- Outpatient
- Home Health (with coverage area maps)
• Languages
- English
- Spanish
- Vietnamese
- Farsi
- Mandarin
- Tagalog
• Insurances Accepted
- HMO
- PPO
- Medicare
- Workers Compensation
• Physician Referral Form (printable PDF)
• Patient Registration Form (able to sign and print)
AGENCIES
• Physical Therapy Coverage Areas with map
• Occupational Therapy Coverage Areas with map
• Speech Therapy Coverage Areas with map
• Inquiry Form that goes directly to Corvela email
- Name
- Title
- Company
- Phone Number
- Email
- Question
• Password access to Credentials & Contact List (editable)
THERAPISTS
• Reasons to work with us
- check example (http://www.ostrandrehab.example/#!therapists/c10my)
- add Referral Bonus
• Career Opportunities editable through an excel worksheet
• Application form that goes directly to Corvela email
- check example (http://www.ostrandrehab.example/#!therapist-application-/cp7d)
FAQ
CONTACT
• Inquiry form
- option of "Agency" or "Patient"
- option of "Home Health Services" or "Outpatient Clinic"
- Question
• Clinic Location & Hours
30587 Marlowe Ave., Suite F
Brenton Falls, CA 90412
Monday - Friday 7:30am - 4:30pm
• Home Health Office Hours
Monday - Friday 9am - 6pm
• Connect to social networks
- Linkedin
https://www.linkedin.com/profile/view?id=517093648&authType=NAME_SEARCH&authToken=qmRt&locale=en_US&trk=tyah&trkInfo=tarId%3A1598304716025%2Ctas%3Acorvela%20physical%20%2Cidx%3A1-1-1
- Facebook
https://www.facebook.com/pages/Corvela-Physical-Therapy/580917264315
Target Market(s)
Adult patients ages 18 to 80 in need of pain management and/or rehab. Home health agencies that contract therapists.
Industry/Entity Type
Architecture
Look and feel

```html
<!DOCTYPE html>
<html lang="en">
<head>
<meta charset="utf-8">
<title>Corvela Physical Therapy</title>
<link rel="stylesheet" href="https://fonts.googleapis.com/css2?family=Open+Sans:wdth,wght@75,300;75,400;75,700;100,400&family=Raleway:wght@800&display=swap">
<style>
:root{
  --brand:#7d0f14;
  --brand-text:#9c1a1f;
  --accent:#c0392b;
  --ink:#222;
  --muted:#777;
  --footer:#141212;
  --white:#fff;
}
*{margin:0;padding:0;box-sizing:border-box}
html,body{width:1200px;height:2432px;overflow:hidden}
body{position:relative;background:var(--white);font-family:"Open Sans",sans-serif;font-stretch:75%;font-weight:300;color:var(--ink)}
.abs{position:absolute}

/* header */
.site-header{left:0;top:0;width:1200px;height:136px;background:var(--white)}
.brand{left:68px;top:44px;display:flex;align-items:center;gap:12px}
.brand-mark{width:18px;height:18px;border-radius:50%;background:var(--brand-text)}
.brand-name{font-weight:400;font-size:36px;color:var(--brand-text);letter-spacing:1px;line-height:1}
.location{top:36px;font-size:13px;line-height:22px;color:var(--brand-text);font-weight:400}
.location .hours{color:#555}
.location-a{left:791px}
.location-b{left:975px}

/* nav */
.main-nav{left:0;top:136px;width:1200px;height:55px;background:var(--brand);display:flex;padding-left:52px}
.main-nav a{color:var(--white);text-decoration:none;font-size:16px;font-weight:400;height:55px;line-height:55px;padding:0 30px;text-transform:uppercase;border-right:1px solid rgba(0,0,0,.15)}
.main-nav a.active{background:#1e1e1e;width:113px;text-align:center;padding:0}

/* hero */
.hero{left:0;top:191px;width:1200px;height:652px;background:linear-gradient(110deg,#e9dcd3 0%,#d9b8a3 45%,#c79a80 75%,#b98a72 100%)}
.hero-title{left:130px;top:566px;font-family:"Raleway",sans-serif;font-stretch:normal;font-weight:800;font-size:36px;line-height:46px;color:var(--white);text-transform:uppercase}
.slider-arrow{top:472px;width:36px;height:36px;border-radius:50%;background:rgba(255,255,255,.45)}
.slider-arrow svg{display:block;margin:9px auto}
.arrow-prev{left:51px}
.arrow-next{left:1111px}

/* setting cards */
.setting-card{top:798px;width:538px;height:151px;background:var(--white);padding:10px 9px}
.setting-card .inner{width:100%;height:129px;background:var(--brand);display:flex;padding:17px 15px}
.setting-card .thumb{width:118px;height:88px;flex:none;background:linear-gradient(135deg,#dcd6d2,#9a8f88)}
.setting-card .copy{margin-left:21px;color:var(--white)}
.setting-card h3{font-weight:400;font-size:18px;text-transform:uppercase;margin-top:-2px}
.setting-card p{font-size:12px;line-height:16px;color:#e07d76;margin-top:6px;width:300px}
.setting-card .more{font-size:12px;font-weight:400;margin-top:6px;display:block}
.card-outpatient{left:54px}
.card-home{left:612px}

/* welcome */
.welcome{left:0;top:992px;width:1200px;height:383px;background:linear-gradient(100deg,#2f2624 0%,#4a3a35 45%,#3a2e2b 100%);text-align:center;color:var(--white)}
.welcome h2{position:absolute;left:0;width:1200px;top:60px;font-weight:400;font-size:24px}
.welcome p{position:absolute;left:178px;width:850px;top:123px;font-size:17px;line-height:25px;font-weight:300}
.btn-red{position:absolute;left:532px;top:271px;width:136px;height:44px;background:var(--accent);color:var(--white);font-size:15px;font-weight:400;line-height:44px;text-transform:uppercase}

/* services */
.services-title{left:0;width:1200px;top:1430px;text-align:center;font-weight:300;font-size:24px;color:#444}
.service{top:1495px;width:255px}
.service .photo{width:255px;height:159px}
.service h3{font-stretch:100%;font-weight:400;font-size:17px;color:var(--brand-text);margin-top:17px}
.service p{font-size:13px;line-height:17px;color:var(--muted);margin-top:8px;width:240px}
.service .btn-outline{display:inline-block;margin-top:13px;width:84px;height:35px;border:1px solid #ccc;background:#f6f6f6;color:var(--brand-text);font-size:13px;font-weight:400;line-height:33px;text-align:center;text-transform:uppercase}
.svc-1{left:52px}.svc-2{left:332px}.svc-3{left:612px}.svc-4{left:892px}

/* email */
.email-band{left:0;top:1873px;width:1200px;height:216px;background:linear-gradient(100deg,#c84a3c 0%,#d4594a 50%,#c44638 100%)}
.email-band h2{position:absolute;left:0;width:1200px;top:40px;text-align:center;color:var(--white);font-weight:300;font-size:25px}
.email-input{position:absolute;left:339px;top:117px;width:355px;height:52px;background:var(--white);color:#888;font-size:17px;font-weight:400;line-height:52px;padding-left:14px}
.email-submit{position:absolute;left:710px;top:117px;width:109px;height:52px;background:#0e0e0e;color:var(--white);font-size:17px;font-weight:400;line-height:52px;text-align:center}

/* footer */
.site-footer{left:0;top:2089px;width:1200px;height:343px;background:linear-gradient(180deg,#1d1a19,var(--footer))}
.footer-nav{position:absolute;left:0;width:1200px;top:64px;text-align:center;font-size:14px;font-weight:400;color:#ddd}
.footer-nav span{padding:0 7px;border-right:1px solid #555}
.footer-nav span:last-child{border-right:0}
.copyright{position:absolute;left:0;width:1200px;top:102px;text-align:center;font-size:13px;font-weight:400;color:#aaa}
.social{position:absolute;top:156px;width:42px;height:42px;border-radius:50%;background:#3a3635}
.social-one{left:535px}.social-two{left:584px}
.footer-address{position:absolute;left:0;width:1200px;top:250px;text-align:center;font-size:13px;line-height:19px;color:#4d4947}
</style>
</head>
<body>

<header class="site-header abs">
  <div class="brand abs"><span class="brand-mark"></span><span class="brand-name">Corvela Physical Therapy</span></div>
  <div class="location location-a abs">30587 MARLOWE AVE., SUITE F<br>BRENTON FALLS, CA 90412<br><span class="hours">MONDAY - FRIDAY 7.30AM - 4.30PM</span></div>
  <div class="location location-b abs">4816 HADLEY BLVD., SUITE D<br>BRENTON FALLS, CA 90418<br><span class="hours">MONDAY - FRIDAY 9AM - 6PM</span></div>
</header>

<nav class="main-nav abs">
  <a class="active">Home</a><a>About</a><a>Patients</a><a>Agencies/Physicians/Clients</a><a>Therapists</a><a>FAQ</a><a>Contact</a>
</nav>

<section class="hero abs" role="img" aria-label="Therapist's hands giving a back massage to a patient"></section>
<div class="slider-arrow arrow-prev abs"><svg width="18" height="18" viewBox="0 0 18 18"><path d="M11 3 5 9l6 6" fill="none" stroke="#777" stroke-width="2.5"/></svg></div>
<div class="slider-arrow arrow-next abs"><svg width="18" height="18" viewBox="0 0 18 18"><path d="M7 3l6 6-6 6" fill="none" stroke="#777" stroke-width="2.5"/></svg></div>
<h1 class="hero-title abs">Personalised &amp; High-Quality<br>Therapy Services</h1>

<article class="setting-card card-outpatient abs"><div class="inner">
  <div class="thumb" role="img" aria-label="Doctor consulting with a patient at the clinic"></div>
  <div class="copy"><h3>Outpatient Clinic</h3><p>Treatment at our clinic with one to one care, modern equipment and a plan built for your recovery</p><span class="more">Read More</span></div>
</div></article>
<article class="setting-card card-home abs"><div class="inner">
  <div class="thumb" role="img" aria-label="Nurse visiting an elderly patient at home"></div>
  <div class="copy"><h3>Home Health Visits</h3><p>Licensed therapists visit you at home to restore strength, balance and daily independence</p><span class="more">Read More</span></div>
</div></article>

<section class="welcome abs" role="img" aria-label="Relaxed client during a massage, dimmed background">
  <h2>WELCOME TO OUR SITE</h2>
  <p>Mes cuml dia sed in lacus ut eniascet ingerto aliiqt es site amet eismod ictor ut ligulate ameti dapibus ticdu nt mtsen lusto dolor ltissim comes cuml dia sed inertio lacusueni ascet dolingerto aliiqt sit amet eism com odictor ut ligulate cot ameti dapibu emo enim ipsam voluptatem voluptas sit aspernatur aut odit aut fugit sed quia consequuntur magni dolores eos qui ratione voluptatem sequi nesciunt. Neque poes cuml dia sed in lacusut eniascet ingerto aliiqt es site amet eismod ictor ut ligulate ameti dapibus ticdu</p>
  <span class="btn-red">Read More</span>
</section>

<h2 class="services-title abs">OUR SERVICES</h2>
<article class="service svc-1 abs">
  <div class="photo" role="img" aria-label="Physical therapist working on a patient's shoulder" style="background:linear-gradient(135deg,#e5ddd6,#b7a79a)"></div>
  <h3>Physical Therapy</h3><p>Restore movement and reduce pain with guided exercise and manual therapy.</p><span class="btn-outline">More Info</span>
</article>
<article class="service svc-2 abs">
  <div class="photo" role="img" aria-label="Therapist helping an older man with a walking exercise" style="background:linear-gradient(135deg,#6f8fa8,#c9a77b)"></div>
  <h3>Occupational Therapy</h3><p>Regain everyday skills at home and work through practical adaptive training.</p><span class="btn-outline">More Info</span>
</article>
<article class="service svc-3 abs">
  <div class="photo" role="img" aria-label="Speech therapist working with a child using cards" style="background:linear-gradient(135deg,#5a4038,#d2a58c)"></div>
  <h3>Speech Therapy</h3><p>Improve speech, language and swallowing in one to one sessions with therapists.</p><span class="btn-outline">More Info</span>
</article>
<article class="service svc-4 abs">
  <div class="photo" role="img" aria-label="Woman receiving a relaxing shoulder massage" style="background:linear-gradient(135deg,#f1dfcf,#d0a07e)"></div>
  <h3>Massage Therapy</h3><p>Ease muscle tension and stress with massage that supports healing and circulation.</p><span class="btn-outline">More Info</span>
</article>

<section class="email-band abs">
  <h2>JOIN OUR EMAIL LIST</h2>
  <div class="email-input">ENTER YOUR EMAIL ADDRESS</div>
  <div class="email-submit">SUBMIT</div>
</section>

<footer class="site-footer abs">
  <div class="footer-nav"><span>HOME</span><span>ABOUT</span><span>PATIENTS</span><span>MASSAGE THERAPY</span><span>THERAPISTS</span><span>FAQ</span><span>CONTACT</span></div>
  <div class="copyright">ALL RIGHTS RESERVED. COPYRIGHTS @ 2014</div>
  <span class="social social-one" aria-label="Social profile"></span>
  <span class="social social-two" aria-label="Social feed"></span>
  <div class="footer-address">30587 MARLOWE AVE., SUITE F, BRENTON FALLS, CA 90412 &nbsp;- &nbsp;MONDAY - FRIDAY 7:30AM - 4:30PM<br>4816 HADLEY BLVD., SUITE D, BRENTON FALLS, CA 90418 &nbsp;- &nbsp;MONDAY - FRIDAY 9AM - 6PM</div>
</footer>

</body>
</html>
```